BrivoMetra. Lantern for the Enterprise Worth. Business card

Professional business card for BrivoMetra (Lantern for the Enterprise Worth)
My rationale: Strategy-> Execution-> Results-> Value that lead to the BrivoMetra name: We put the Lantern for the Enterprise Worth.
We deliver value to our customers helping them at defining a good strategy (cyan arrow). 90% of well formulated strategies fail due to poor execution so we also consider strategical execution very important (green arrow). Due to the execution we obtain the results (blue arrow). Finally, the results provide feedback to redefine strategy, and the new strategy has to be executed and new results obtained providing new feedback and on and on. It's like a wheel that finally, must create corporate value: value for shareholders, staholders, employees, providers...-

Target Market(s)

CEOs and steering comitees , invewrnent funds

Industry/Entity Type

Business Consultant

Contact Information for Business Card

Teodoro Vinschetti
CEO & Founder
teodoro.vinschetti@brivometra-example.com
Mobile: +34 655.802.913
www.brivometra-example.com

Colors

Designer to choose colors to be used in the design.

Requirements
Nice to have
• Nice to hace the words: INSIGHT, DELIVERY, OUTCOMES
• Nice to vave the claim: Lantern for the Enterprise Worth
• The three colors should be shown:
• cyan for STRATEGY
• green for EXECUTION
• blue for RESULTS
Should not have
• Complete black background

```html
<!DOCTYPE html>
<html lang="en">
<head>
<meta charset="utf-8">
<title>BrivoMetra — Business Card</title>
<link rel="stylesheet" href="https://fonts.googleapis.com/css2?family=Arimo:wght@400;700&display=swap">
<style>
  :root {
    --backdrop: #0b0b0c;
    --card: #2a2a2c;
    --edge-blue: #1d3fc4;
    --brand-blue: #0a3fbf;
    --tagline-cyan: #1fa6d8;
    --name-green: #8cc63f;
    --ink-light: #e9e9e9;
    --emboss-grey: #55565a;
  }
  * { box-sizing: border-box; margin: 0; padding: 0; }
  html, body {
    width: 1200px;
    height: 822px;
    overflow: hidden;
    background: var(--backdrop);
    font-family: "Arimo", Arial, sans-serif;
  }
  .stage {
    position: relative;
    width: 1200px;
    height: 822px;
    display: flex;
    align-items: center;
    justify-content: center;
    gap: 60px;
  }
  .card {
    width: 500px;
    height: 286px;
    background: var(--card);
    border: 2px solid var(--edge-blue);
    border-radius: 2px;
    position: relative;
    box-shadow: 0 18px 40px rgba(0,0,0,0.6);
  }
  .card-front {
    display: flex;
    flex-direction: column;
    align-items: center;
    justify-content: center;
    text-align: center;
  }
  .brand-name {
    color: var(--brand-blue);
    font-weight: 700;
    font-size: 46px;
    letter-spacing: -1px;
    line-height: 1;
  }
  .tagline {
    color: var(--tagline-cyan);
    font-size: 12px;
    letter-spacing: 0.8px;
    margin-top: 4px;
  }
  .person-name {
    color: var(--name-green);
    font-size: 20px;
    margin-top: 22px;
  }
  .person-role {
    color: var(--ink-light);
    font-size: 13px;
    margin-top: 3px;
  }
  .contact {
    list-style: none;
    color: var(--ink-light);
    font-size: 12.5px;
    line-height: 1.35;
    margin-top: 16px;
  }
  .card-back {
    display: flex;
    align-items: center;
    justify-content: center;
    gap: 14px;
  }
  .back-mark {
    width: 26px;
    height: 26px;
    border-radius: 50%;
    background: var(--emboss-grey);
  }
  .back-name {
    color: var(--emboss-grey);
    font-weight: 700;
    font-size: 48px;
    letter-spacing: -1px;
  }
</style>
</head>
<body>
  <main class="stage">
    <section class="card card-front" aria-label="Business card front">
      <div class="brand-name">BrivoMetra</div>
      <div class="tagline">INSIGHT, DELIVERY, OUTCOMES</div>
      <div class="person-name">Teodoro Vinschetti</div>
      <div class="person-role">CEO &amp; Founder</div>
      <ul class="contact">
        <li>+34 655.802.913</li>
        <li>teodoro.vinschetti@brivometra-example.com</li>
        <li>www.brivometra-example.com</li>
      </ul>
    </section>
    <section class="card card-back" aria-label="Business card back">
      <span class="back-mark"></span>
      <span class="back-name">BrivoMetra</span>
    </section>
  </main>
</body>
</html>
```